Business Card Design Project

Business Card
We are rebranding with a new logo
Industry/Entity Type
Business
Contact Information for Business Card
Dennis Marlow +61 427581962 dennis@qovo.com.au P.O. Box 872 Kelvindale QLD 4309
Requirements
Must have
- Logo

```html
<!DOCTYPE html>
<html lang="en">
<head>
<meta charset="utf-8">
<title>Qovo International – Business Card</title>
<link rel="stylesheet" href="https://fonts.googleapis.com/css2?family=Lato:wght@400;700;900&display=swap">
<style>
  :root {
    --backdrop: #cbcbcb;
    --card: #ffffff;
    --ink: #1d1d1f;
    --brand-navy: #0d4f7a;
    --band-blue: #1ea8e0;
    --band-light: #8ad8f7;
    --icon-blue: #62c3ee;
  }
  * { box-sizing: border-box; margin: 0; padding: 0; }
  html, body {
    width: 1200px;
    height: 1000px;
    overflow: hidden;
    background: var(--backdrop);
    font-family: "Lato", sans-serif;
  }
  .business-card {
    position: absolute;
    left: 60px;
    top: 192px;
    width: 1080px;
    height: 616px;
    background: var(--card);
    box-shadow: 8px 10px 18px rgba(0,0,0,0.28);
  }
  .brand {
    position: absolute;
    left: 109px;
    top: 278px;
    display: flex;
    align-items: center;
    gap: 12px;
    white-space: nowrap;
    color: var(--brand-navy);
    font-weight: 900;
    font-size: 28px;
    line-height: 36px;
    letter-spacing: 0.5px;
  }
  .brand-dot {
    width: 24px;
    height: 24px;
    border-radius: 50%;
    background: var(--band-blue);
    flex: none;
  }
  .contact-line {
    position: absolute;
    left: 653px;
    display: flex;
    align-items: flex-start;
    gap: 24px;
    color: var(--ink);
    font-weight: 700;
    font-size: 25px;
    letter-spacing: 1px;
    line-height: 40px;
    white-space: nowrap;
  }
  .contact-line svg { flex: none; margin-top: 7px; }
  .contact-phone { top: 71px; }
  .contact-email { top: 137px; }
  .contact-address { top: 442px; }
  .name-band {
    position: absolute;
    left: 606px;
    top: 200px;
    width: 474px;
    height: 200px;
    background: var(--band-blue);
    border-radius: 8px 0 0 8px;
    box-shadow: 0 4px 6px rgba(0,0,0,0.15);
    overflow: hidden;
  }
  .band-accent {
    position: absolute;
    right: 0;
    top: 0;
    width: 122px;
    height: 100%;
    background: linear-gradient(90deg, rgba(138,216,247,0) 0%, var(--band-light) 100%);
  }
  .holder-name {
    position: absolute;
    left: 42px;
    top: 74px;
    color: #ffffff;
    font-size: 40px;
    line-height: 50px;
    letter-spacing: 1.5px;
    font-weight: 400;
    white-space: nowrap;
  }
  .holder-name strong { font-weight: 900; }
</style>
</head>
<body>
  <main class="business-card">
    <div class="brand">
      <span class="brand-dot"></span>
      <span class="brand-name">Qovo International</span>
    </div>

    <div class="contact-line contact-phone">
      <svg width="26" height="26" viewBox="0 0 26 26" aria-hidden="true">
        <circle cx="13" cy="13" r="13" fill="var(--icon-blue)"/>
        <path d="M9 7c1 0 2 2.5 2 3s-1 1-1 1.5c.5 1.5 2 3 3.5 3.5.5 0 1-1 1.5-1s3 1 3 2-1 2.5-2.5 2.5C11 18.5 7.5 15 7.5 9.5 7.5 8 8 7 9 7z" fill="#fff"/>
      </svg>
      <span>+61 427581962</span>
    </div>

    <div class="contact-line contact-email">
      <svg width="26" height="26" viewBox="0 0 26 26" aria-hidden="true">
        <circle cx="13" cy="13" r="13" fill="var(--icon-blue)"/>
        <rect x="7" y="9" width="12" height="8.5" rx="1" fill="#fff"/>
        <path d="M7.5 9.5 13 14l5.5-4.5" stroke="var(--icon-blue)" stroke-width="1.2" fill="none"/>
      </svg>
      <span>dennis@qovo.com.au</span>
    </div>

    <div class="name-band">
      <div class="band-accent" role="img" aria-label="Light blue faceted geometric pattern"></div>
      <p class="holder-name"><strong>Dennis</strong> Marlow</p>
    </div>

    <div class="contact-line contact-address">
      <svg width="26" height="26" viewBox="0 0 26 26" aria-hidden="true">
        <circle cx="13" cy="13" r="13" fill="var(--icon-blue)"/>
        <circle cx="13" cy="13" r="6.5" fill="none" stroke="#fff" stroke-width="1.3"/>
        <ellipse cx="13" cy="13" rx="3" ry="6.5" fill="none" stroke="#fff" stroke-width="1.1"/>
        <path d="M6.5 13h13M7.5 10h11M7.5 16h11" stroke="#fff" stroke-width="1"/>
      </svg>
      <span>P.O. Box 872<br>Kelvindale QLD 4309</span>
    </div>
  </main>
</body>
</html>
```